Lumora Learning Web Design Project

Who We are:
Lumora Learning is education information portal/ magazine, providing information about the Chinese and International education markets. Our aim is to help school principals improve there curriculum, and parents in understanding this curriculum.

Project Brief:
The site will include education news updates, educational services, curriculum developments and overseas study. We hope the site represents the cross cultural bridge between the west and east. The site will cover both the Sciences and Arts.

Note:
The logo design competition is also underway so we only need the website design

What We want:
This competition is for Design only no coding!
Design a home page based on Template 1,2 or 3. I only need to select one.
The design of an article page.

Optional
Design a Microsoft Windows metro style splash page.

Sites We like:
http://www.kavelin.com.cn/kavelinlingo/default.aspx
http://www.brixtalacademia.co.uk/
http://qrpv.norvatestudio.net/

Template Explanations:
Template 1-
The main information has a dynamic sliding category view that when clicked displays the relevant info.
In addition to the main upper menu it also has a left hand sliding menu that pops out on click or gesture

Template 2-
Has limited number of Articles most of the menus are drop downs from the top menu

Template 3-
No Top menu

Target Market(s)

Teachers, principals and parents

Industry/Entity Type

Education

Requirements
Should not have
• kindergarten preschool feel

```html
<!DOCTYPE html>
<html lang="en">
<head>
<meta charset="utf-8">
<title>Lumora Learning — Home</title>
<link rel="stylesheet" href="https://fonts.googleapis.com/css2?family=Montserrat:wght@300;400;600;700&display=swap">
<style>
:root{
  --lime:#c8c92f;
  --olive:#a9a92a;
  --olive-dark:#7d7d12;
  --purple:#5e1a8c;
  --orange:#f26a1b;
  --blue:#1565c0;
  --pink:#d1116c;
  --red:#e8000b;
  --grey-panel:#d9d9d9;
  --grey-band:#bdbdbd;
  --grey-footer:#cbcbcb;
  --ink:#333;
  --ink-soft:#777;
  --white:#fff;
}
*{margin:0;padding:0;box-sizing:border-box}
html,body{width:683px;height:1200px;overflow:hidden;background:var(--white)}
body{position:relative;font-family:"Montserrat",Arial,sans-serif;color:var(--ink)}
.abs{position:absolute}
a{color:inherit;text-decoration:none}

/* header */
.brand{left:37px;top:30px;font-size:22px;font-weight:300;color:#8a8a8a;line-height:1.1;letter-spacing:.3px;white-space:nowrap}
.brand-mark{display:inline-block;width:12px;height:12px;border-radius:50%;background:#8a8a8a;margin-right:6px;vertical-align:middle}
.util{top:12px;font-size:6px;line-height:8px;color:#777;letter-spacing:0;white-space:nowrap}
.search-box{left:378px;top:9px;width:81px;height:13px;border:1px solid #ccc}
.circle-ico{width:13px;height:13px;border:1px solid #999;border-radius:50%}
.lang-num{left:510px;top:9px;font-size:6px;text-align:center;line-height:11px;color:#777}

.nav{left:250px;top:84px;width:433px;height:16px}
.nav-label{top:88px;font-size:6.5px;color:var(--white);font-weight:600;letter-spacing:.2px;white-space:nowrap}

/* hero */
.hero-panel{left:0;top:100px;width:250px;height:233px;background:var(--lime)}
.hero-photo{left:250px;top:100px;width:433px;height:233px;background:linear-gradient(100deg,#3a3a3a 0%,#e9e9e9 18%,#bdbdbd 40%,#f0f0f0 55%,#2c2620 85%,#1e1a16 100%)}
.hero-title{left:33px;top:146px;font-size:27px;line-height:25px;font-weight:300;color:var(--white);letter-spacing:-.3px;white-space:nowrap}
.hero-title strong{font-weight:700;color:var(--olive-dark)}
.hero-sub{left:33px;top:240px;font-size:14.5px;line-height:17px;font-weight:300;color:var(--white);white-space:nowrap}
.hero-more{left:33px;top:297px;font-size:6.5px;font-weight:700;color:var(--white)}
.dot{top:316px;width:7px;height:7px;border-radius:50%;border:1px solid #fff;background:#777}

/* events */
.side-shapes{left:0;top:333px;width:250px;height:325px}
.events-title{left:33px;top:387px;font-size:19px;font-weight:700;color:#555;letter-spacing:.5px}
.date-badge{left:167px;top:363px;width:46px;height:47px;background:var(--white);box-shadow:2px 3px 0 rgba(0,0,0,.12);text-align:center}
.date-month{height:11px;background:#555;color:#fff;font-size:6.5px;line-height:11px}
.date-day{font-size:25px;font-weight:700;color:#666;line-height:34px}
.ev{left:33px;font-size:7px;color:#444;white-space:nowrap}
.ev b{font-weight:700;color:#444}
.ev-cat{top:446px;font-weight:700;font-size:6.5px}
.ev-title{top:453px;font-size:14px;line-height:16px;font-weight:300;color:#555}
.ev-body{top:484px;line-height:12px;font-size:6.8px}
.ev-all{top:600px;font-weight:700;font-size:6px}
.arrow{width:0;height:0;border-left:3px solid transparent;border-right:3px solid transparent}

/* articles */
.thumb{width:128px;height:84px;top:362px}
.tag{top:446px;height:11px;font-size:6px;line-height:11px;color:#fff;font-weight:600;padding-left:8px;white-space:nowrap}
.article{top:479px;width:130px}
.kicker{font-size:10px;font-weight:700;letter-spacing:.2px}
.a-title{font-size:12px;font-weight:400;color:#333;line-height:13px;white-space:nowrap}
.lead{margin-top:10px;font-size:6.8px;font-weight:700;line-height:12px;color:#555;letter-spacing:-.1px}
.body{margin-top:0;font-size:6.8px;line-height:12px;color:#777;letter-spacing:-.1px}
.more{margin-top:8px;font-size:6px;font-weight:700;color:#555}
.divider-v{width:1px;background:#ddd}

/* arts */
.arts-bar{left:0;top:658px;width:462px;height:31px}
.arts-label{left:33px;top:670px;font-size:9px;font-weight:700;color:#fff}
.arts-photo{left:0;top:689px;width:440px;height:314px;background:radial-gradient(ellipse at 35% 55%,#d86aa8 0%,#a8306f 30%,#5a1020 60%,#2a0608 100%)}
.overlay{left:231px;top:745px;width:217px;height:145px;background:rgba(40,40,40,.88);padding:18px 12px 18px 22px}
.overlay h2{font-size:19px;line-height:22px;font-weight:300;color:#fff;letter-spacing:-.2px;white-space:nowrap}
.overlay p{margin-top:10px;font-size:10.5px;line-height:12px;font-weight:300;color:#fff}
.arts-tag{left:402px;top:991px;width:38px;height:12px;background:var(--red);font-size:6px;color:#fff;line-height:12px;text-align:center;font-weight:600;white-space:nowrap}
.about{left:498px;top:689px;width:132px}
.about .kicker{color:var(--red)}
.about-name{margin-top:9px;font-size:12px;line-height:13px;font-weight:400;color:#333}

/* footer */
.footer{left:0;top:1003px;width:683px;height:197px;background:var(--grey-footer)}
.f-head{font-size:8.5px;color:#666;font-weight:400;white-space:nowrap}
.f-list{list-style:none;font-size:6px;color:#777;line-height:16px;margin-top:6px;white-space:nowrap}
.f-list .on{font-weight:700;color:#555}
.f-line{font-size:6px;color:#777;white-space:nowrap}
.field{background:#fff}
.f-label{font-size:5.5px;color:#777;padding:3px 4px}
</style>
</head>
<body>

<!-- header -->
<div class="abs brand"><span class="brand-mark"></span>Lumora Learning</div>
<span class="abs util" style="left:344px">SEARCH</span>
<div class="abs search-box"></div>
<span class="abs util" style="left:470px">LANGUAGE</span>
<div class="abs circle-ico lang-num">0</div>
<span class="abs util" style="left:540px">FOLLOW US</span>
<div class="abs circle-ico" style="left:582px;top:9px"></div>
<div class="abs circle-ico" style="left:600px;top:9px"></div>
<div class="abs circle-ico" style="left:618px;top:9px"></div>
<div class="abs circle-ico" style="left:636px;top:9px"></div>

<svg class="abs nav" viewBox="0 0 433 16" aria-hidden="true">
  <polygon points="8,0 73,0 65,16 0,16" fill="var(--purple)"/>
  <polygon points="73,0 148,0 140,16 65,16" fill="var(--orange)"/>
  <polygon points="148,0 263,0 255,16 140,16" fill="var(--blue)"/>
  <polygon points="263,0 348,0 340,16 255,16" fill="var(--pink)"/>
  <polygon points="348,0 433,0 433,16 340,16" fill="var(--lime)"/>
</svg>
<nav>
  <a class="abs nav-label" style="left:275px">NEWS</a>
  <a class="abs nav-label" style="left:337px">SERVICES</a>
  <a class="abs nav-label" style="left:413px">OVERSEAS STUDIES</a>
  <a class="abs nav-label" style="left:524px">CURRICULUM</a>
  <a class="abs nav-label" style="left:615px">CONTACTS</a>
</nav>

<!-- hero -->
<div class="abs hero-panel"></div>
<div class="abs hero-photo" role="img" aria-label="Photo of backlit study-abroad banners for several countries with a silhouetted student reading"></div>
<h1 class="abs hero-title">EUM LAORET<br><strong>IUDICABIT</strong><br>POSIDONIUM</h1>
<p class="abs hero-sub">EUM LAOREET IUDICABIT<br>POSIDONIUM QUO TE.</p>
<a class="abs hero-more">READ MORE HERE »</a>
<span class="abs dot" style="left:623px"></span>
<span class="abs dot" style="left:634px;background:var(--lime)"></span>
<span class="abs dot" style="left:645px;background:#fff"></span>

<!-- events panel -->
<svg class="abs side-shapes" viewBox="0 0 250 325" aria-hidden="true">
  <polygon points="0,0 250,0 225,29 0,29" fill="var(--olive)"/>
  <rect x="0" y="29" width="225" height="268" fill="var(--grey-panel)"/>
  <polygon points="0,297 225,297 250,325 0,325" fill="var(--grey-band)"/>
</svg>
<h2 class="abs events-title">EVENTS</h2>
<div class="abs date-badge"><div class="date-month">JULY</div><div class="date-day">09</div></div>
<div class="abs arrow" style="left:33px;top:433px;border-bottom:4px solid #444"></div>
<div class="abs ev ev-cat">CONFERENCES</div>
<div class="abs ev ev-title">EVENT MAIN TITLE</div>
<div class="abs ev ev-body">
  <b>DATE</b> › 15 JULY<br><b>LOCATION</b> › XXXXXX (CHINA)<br><br>
  <b>MAIN INFO</b> › Eum ex, laoreet iudicabit<br>posid onium quote. Mei ex legere civibus<br>phaedrum. Id eam putent conceptam.<br>
  <b>WEBSITE</b> › www.learnaheadnow.org
</div>
<div class="abs arrow" style="left:33px;top:575px;border-top:4px solid #444"></div>
<a class="abs ev ev-all">ALL EVENTS HERE ››</a>

<!-- articles -->
<div class="abs thumb" style="left:293px;background:linear-gradient(135deg,#b02a2a,#e7c6b0 50%,#8a2020)" role="img" aria-label="Photo of two students reading together"></div>
<div class="abs tag" style="left:359px;width:62px;background:var(--purple)">+ NEWS</div>
<div class="abs thumb" style="left:499px;background:linear-gradient(180deg,#6f8f5a,#9aa3a8 45%,#3c3f44)" role="img" aria-label="Photo of a group of students outdoors"></div>
<div class="abs tag" style="left:525px;width:102px;background:var(--blue)">+ OVERSEAS STUDIES</div>
<div class="abs divider-v" style="left:462px;top:370px;height:260px"></div>

<article class="abs article" style="left:293px">
  <div class="kicker" style="color:var(--purple)">NEWS</div>
  <h3 class="a-title">ARTICLE MAIN TITLE</h3>
  <p class="lead">EUM EX, LAOREET IUDICABIT POSIDONIUM QUO TE. MEI EX LEGERE CIVIBUS PHAEDRUM. ID EAM PUTENT CONCEPTAM.</p>
  <p class="body">Ad malis nihil epicurei dolorum torquatos ut, cu pro movet debitis graecis. Diam dicat nam ei, qui tibique eligendi salutandi eu. (...)</p>
  <p class="more">READ MORE HERE ››</p>
</article>
<article class="abs article" style="left:499px">
  <div class="kicker" style="color:var(--blue)">OVERSEAS STUDIES</div>
  <h3 class="a-title">ARTICLE MAIN TITLE</h3>
  <p class="lead">EUM EX, LAOREET IUDICABIT POSIDONIUM QUO TE. MEI EX LEGERE CIVIBUS PHAEDRUM. ID EAM PUTENT CONCEPTAM.</p>
  <p class="body">Ad malis nihil epicurei dolorum torquatos ut, cu pro movet debitis graecis. Diam dicat nam ei, qui tibique eligendi salutandi eu. (...)</p>
  <p class="more">READ MORE HERE ››</p>
</article>

<!-- arts -->
<svg class="abs arts-bar" viewBox="0 0 462 31" aria-hidden="true">
  <polygon points="0,0 462,0 440,31 0,31" fill="var(--red)"/>
</svg>
<div class="abs" style="left:462px;top:658px;width:178px;height:1px;background:#ddd"></div>
<div class="abs arts-label">ARTS</div>
<div class="abs arts-photo" role="img" aria-label="Stage photo of dancers in flowing pink costumes at a dance festival"></div>
<div class="abs overlay">
  <h2>DANCE FESTIVAL</h2>
  <p>EUM EX, LAOREET IUDICABIT POSID ONIUM QUO TE. MEI EX LEGERE CIVIBUS PHAEDRUM. ID EAM PUTENT CONCEPTAM. AD MALIS NIHIL</p>
</div>
<div class="abs arts-tag">+ ARTS ››</div>

<section class="abs about">
  <div class="kicker">ABOUT US</div>
  <div class="about-name">LUMORA<br>LEARNING</div>
  <p class="lead" style="margin-top:14px">EUM EX, LAOREET IUDICABIT POSID ONIUM QUO TE. MEI EX LEGERE CIVIBUS PHAEDRUM. ID EAM PUTENT CONCEPTAM. AD MALIS NIHIL EPICUREI DOLORUM TORQUATOS UT, CU PRO MOVET DEBITIS GRAECIS.</p>
  <p class="body">Ad malis nihil epicurei dolorum torquatos ut, cu pro movet debitis graecis. Diam dicat nam ei, qui tibique eligendi salutandi eu.<br>Ad malis nihil epicurei dolorum torquatos ut, cu pro movet debitis graecis Diam dicat nam ei, qui tibique Diam dicat nam ei, qui tibiqueeligendi salutandi eu (...)</p>
  <p class="more" style="margin-top:20px">READ MORE HERE ››</p>
</section>

<!-- footer -->
<footer class="abs footer">
  <div class="abs" style="left:42px;top:42px">
    <div class="f-head">MAIN OPTIONS</div>
    <ul class="f-list"><li>» NEWS</li><li>» SERVICES</li><li>» OVERSEAS STUDIES</li><li>» CURRICULUM</li><li>» CONTACTS</li></ul>
  </div>
  <div class="abs divider-v" style="left:131px;top:42px;height:118px;background:#aaa"></div>
  <div class="abs" style="left:153px;top:42px">
    <div class="f-head">OTHER OPTIONS</div>
    <ul class="f-list"><li>» EVENTS</li><li>» ARTS</li><li>» ABOUT US</li><li>» SITE MAP</li></ul>
    <div class="f-head" style="margin-top:10px">CHOOSE LANGUAGE</div>
    <ul class="f-list"><li>» 中國的</li><li class="on">›› ENGLISH</li></ul>
  </div>
  <div class="abs divider-v" style="left:261px;top:42px;height:118px;background:#aaa"></div>
  <div class="abs" style="left:280px;top:42px">
    <div class="f-head">CONTACTS</div>
    <ul class="f-list"><li class="on">XXXXXXXXXX</li><li>XXXXXXXXXXXXX</li><li>XXXXXXXX &nbsp;|&nbsp; CHINA</li></ul>
    <ul class="f-list" style="margin-top:12px"><li>Phone: +XXXXXXXXXXXX</li><li>Telefax: +XXXXXXXXXXXX</li><li>Email: XXXXXXXXXXX@XXXXX.COM</li></ul>
  </div>
  <div class="abs" style="left:487px;top:41px;width:163px">
    <div class="f-head" style="text-align:center">GIVE US YOUR FEEDBACK</div>
    <div class="field f-label" style="margin-top:4px;height:13px">E-MAIL</div>
    <div class="field f-label" style="margin-top:3px;height:41px">COMMENT</div>
    <div class="f-line" style="text-align:right;margin-top:4px;font-size:5.5px">SUBMIT</div>
    <div class="f-head" style="text-align:center;margin-top:8px">FOLLOW US</div>
  </div>
  <div class="abs circle-ico" style="left:537px;top:150px"></div>
  <div class="abs circle-ico" style="left:555px;top:150px"></div>
  <div class="abs circle-ico" style="left:573px;top:150px"></div>
  <div class="abs circle-ico" style="left:591px;top:150px"></div>
  <div class="abs f-line" style="left:505px;top:181px;font-size:5px">© COPYRIGHTS 2013 &nbsp;|&nbsp; ALL RIGHTS RESERVED</div>
</footer>

</body>
</html>
```